Creative and Fun Farm Metal Signage in the Barn

This will be featured in the farm. to make it more unique, the measurement will be 90cm x 60cm. This sign will be made by Metal and display inside the Barn. do have 2 A4 pockets available for them to slip in the cow's birth certificate. please make it fun and professional look. i have attached few photos that show rough idea of how we want it to be.

Target Market(s)

Restaurants or Hotels

Requirements
Must have
• Include 2 A4s certificate as stated, the logo and reserver for logo as well..
Nice to have
• This is a design of Signage where we will put it up in the barn.. this will consist a logo, Reserved by, and 2 A4 paper to slip in. be creative on the design

```html
<!DOCTYPE html>
<html lang="en">
<head>
<meta charset="utf-8">
<title>Tallowgrass Barn Sign</title>
<link rel="stylesheet" href="https://fonts.googleapis.com/css2?family=Allerta+Stencil&family=Cinzel:wght@400;700&display=swap">
<style>
  :root {
    --backdrop: #d4d5d7;
    --metal-dark: #1f1f20;
    --metal-mid: #3a3a3c;
    --etch: #d9d9db;
    --etch-soft: #bfc0c2;
    --stencil: #8d8d90;
    --pocket-fill: rgba(217,217,219,0.08);
    --card: #ffffff;
    --card-ink: #1c1c1c;
    --card-accent: #8c7b4e;
  }
  html, body {
    margin: 0;
    padding: 0;
    overflow: hidden;
    background: var(--backdrop);
  }
  .stage {
    position: relative;
    width: 1200px;
    height: 900px;
    overflow: hidden;
    background: var(--backdrop);
  }
  .sign-plate {
    position: absolute;
    left: 91px;
    top: 111px;
    width: 1018px;
    height: 678px;
    border-radius: 53px;
    background:
      repeating-linear-gradient(96deg, rgba(255,255,255,0.05) 0 1px, rgba(0,0,0,0) 1px 3px, rgba(0,0,0,0.08) 3px 4px, rgba(0,0,0,0) 4px 7px),
      linear-gradient(160deg, var(--metal-mid) 0%, var(--metal-dark) 45%, var(--metal-mid) 75%, var(--metal-dark) 100%);
  }
  .sign-art {
    position: absolute;
    left: 0;
    top: 0;
  }
  .headline {
    position: absolute;
    left: 91px;
    width: 1018px;
    top: 138px;
    margin: 0;
    text-align: center;
    font-family: "Cinzel", serif;
    font-weight: 700;
    font-size: 38px;
    letter-spacing: 1px;
    color: var(--etch);
    white-space: nowrap;
  }
  .brand-name {
    position: absolute;
    left: 141px;
    width: 668px;
    top: 296px;
    margin: 0;
    text-align: center;
    font-family: "Cinzel", serif;
    font-weight: 700;
    font-size: 74px;
    line-height: 1;
    color: var(--etch);
    white-space: nowrap;
  }
  .reserved-label {
    position: absolute;
    left: 135px;
    width: 390px;
    top: 525px;
    text-align: center;
    font-family: "Allerta Stencil", sans-serif;
    font-size: 33px;
    letter-spacing: 3px;
    color: var(--stencil);
    white-space: nowrap;
  }
  .client-card {
    position: absolute;
    left: 156px;
    top: 578px;
    width: 342px;
    height: 143px;
    border-radius: 10px;
    background: var(--card);
    display: flex;
    align-items: center;
    justify-content: center;
    gap: 12px;
  }
  .client-mark {
    width: 16px;
    height: 16px;
    background: var(--card-accent);
  }
  .client-name {
    font-family: "Cinzel", serif;
    font-weight: 400;
    font-size: 27px;
    color: var(--card-ink);
    white-space: nowrap;
  }
</style>
</head>
<body>
<main class="stage">
  <div class="sign-plate"></div>

  <svg class="sign-art" width="1200" height="900" viewBox="0 0 1200 900">
    <defs>
      <symbol id="seven-star" viewBox="-1 -1 2 2">
        <polygon points="0,-1 0.195,-0.405 0.782,-0.623 0.439,-0.1 0.975,0.223 0.352,0.281 0.434,0.901 0,0.45 -0.434,0.901 -0.352,0.281 -0.975,0.223 -0.439,-0.1 -0.782,-0.623 -0.195,-0.405" fill="var(--etch)"/>
      </symbol>
      <linearGradient id="ornament-tone" x1="0" y1="0" x2="1" y2="1">
        <stop offset="0" stop-color="#c9cacc"/>
        <stop offset="1" stop-color="#9d9ea1"/>
      </linearGradient>
    </defs>

    <g class="southern-cross">
      <use href="#seven-star" x="920" y="258" width="106" height="106"/>
      <use href="#seven-star" x="856" y="394" width="28" height="28"/>
      <use href="#seven-star" x="150" y="425" width="40" height="40"/>
      <use href="#seven-star" x="412" y="455" width="36" height="36"/>
      <use href="#seven-star" x="560" y="520" width="42" height="42"/>
      <use href="#seven-star" x="720" y="470" width="48" height="48"/>
    </g>

    <g class="certificate-pockets">
      <g class="a4-pocket" role="img" aria-label="A4 certificate pocket">
        <rect x="550" y="598" width="94" height="133" rx="6" fill="var(--pocket-fill)" stroke="var(--etch-soft)" stroke-width="4"/>
        <line x1="562" y1="612" x2="632" y2="612" stroke="var(--etch-soft)" stroke-width="3"/>
      </g>
      <g class="a4-pocket" role="img" aria-label="A4 certificate pocket">
        <rect x="656" y="598" width="94" height="133" rx="6" fill="var(--pocket-fill)" stroke="var(--etch-soft)" stroke-width="4"/>
        <line x1="668" y1="612" x2="738" y2="612" stroke="var(--etch-soft)" stroke-width="3"/>
      </g>
    </g>

    <g class="corner-arcs">
      <path class="arc-band" d="M 762 780 A 310 360 0 0 1 1072 420 L 1072 438 A 288 342 0 0 0 784 780 Z" fill="var(--etch)"/>
      <path class="arc-band" d="M 809 780 A 263 317 0 0 1 1072 463 L 1072 483 A 239 297 0 0 0 833 780 Z" fill="var(--etch)"/>
      <path class="corner-ornament" role="img" aria-label="Etched scrollwork ornament" d="M 873 780 A 199 229 0 0 1 1072 551 L 1072 780 Z" fill="url(#ornament-tone)"/>
    </g>

    <path class="reserved-frame" d="M 340 748 L 507 748 A 18 18 0 0 0 525 730 L 525 542 A 18 18 0 0 0 507 524 L 153 524 A 18 18 0 0 0 135 542 L 135 730 A 18 18 0 0 0 153 748 L 330 748" fill="none" stroke="var(--etch-soft)" stroke-width="7"/>
  </svg>

  <h1 class="headline">• AUSTRALIAN PREMIUM WAGYU BEEF •</h1>
  <p class="brand-name">TALLOWGRASS</p>

  <div class="reserved-label">RESERVED FOR</div>
  <div class="client-card">
    <span class="client-mark"></span>
    <span class="client-name">KESTREL BAY HOTELS</span>
  </div>
</main>
</body>
</html>
```